Thistleby's Organic's. I make and sell organic bath & body products. Nourishing bath & body products. Products are soaps, scrubs, lip balms, bath salts, baby & mother products (belly balm, nipple balm, diaper balm, baby bath soak, chest rub,) . I use botanical and or herbs in all my recipes. I create my own recipes. I like muted colors...but I would like something that will get your attention. I like the colors green and brown, but open to any other colors. I would also like to get information about labels (different sizes for my products) I do like the pasley print and maybe even a cute owl.

Target Market(s)

women, pregnant and nursing women, women with children and men

Industry/Entity Type

Baby

Contact Information for Business Card

Rhoda Quillmore
527-614-2870,rquillmore@lumaweb.net
rquillmore@lumaweb.net

Font styles to use
Other font styles liked:
• bree

Requirements
Must have
• Thistleby's Organic's, nourishing bath & body products. It needs to get a person attention. I would like to see cards that are hip and fun. I would also like to view cards that are classy. I do like muted colors but I do have an open mind (use any color you think would be right) So far a lot of the cards have had leaves....I really do not like that design.
Nice to have
• ???pasley in the background ?cute owl
Should not have
• leaves

```html
<!DOCTYPE html>
<html lang="en">
<head>
<meta charset="UTF-8">
<title>Thistleby's Organic's – Business Card</title>
<link href="https://fonts.googleapis.com/css2?family=Federant&family=Roboto+Condensed:wght@400&display=swap" rel="stylesheet">
<style>
  :root {
    --backdrop: #1f1f1f;
    --card-green: #c9e1aa;
    --olive: #8b7d22;
    --charcoal: #33363a;
    --rule: #9a9a78;
  }
  html, body {
    margin: 0;
    padding: 0;
    width: 1200px;
    height: 800px;
    overflow: hidden;
    background: var(--backdrop);
  }
  .business-card {
    position: absolute;
    left: 50px;
    top: 88px;
    width: 1100px;
    height: 625px;
    border-radius: 46px;
    background: var(--card-green);
    overflow: hidden;
  }
  .brand-name {
    position: absolute;
    left: 72px;
    top: 112px;
    margin: 0;
    font-family: "Federant", serif;
    font-weight: 400;
    font-size: 52px;
    line-height: 1.2;
    white-space: nowrap;
    color: var(--olive);
    letter-spacing: 0.5px;
  }
  .owner-name {
    position: absolute;
    left: 72px;
    top: 335px;
    margin: 0;
    font-family: "Federant", serif;
    font-weight: 400;
    font-size: 44px;
    line-height: 1.2;
    white-space: nowrap;
    color: var(--charcoal);
  }
  .contact-list {
    position: absolute;
    left: 78px;
    top: 440px;
    margin: 0;
    padding: 0;
    list-style: none;
    font-family: "Roboto Condensed", sans-serif;
    font-size: 30px;
    color: var(--charcoal);
  }
  .contact-item {
    display: flex;
    align-items: center;
    height: 46px;
    white-space: nowrap;
  }
  .contact-rule {
    display: inline-block;
    width: 112px;
    border-top: 2px dotted var(--rule);
    margin-right: 10px;
  }
  .owl-illustration {
    position: absolute;
    left: 655px;
    top: 150px;
    width: 420px;
    height: 455px;
    border-radius: 30px;
    background: radial-gradient(ellipse at 60% 45%, #b9c77e 0%, #c3d696 55%, var(--card-green) 80%);
  }
</style>
</head>
<body>
  <section class="business-card">
    <h1 class="brand-name">Thistleby's Organic's</h1>
    <h2 class="owner-name">Rhoda Quillmore</h2>
    <ul class="contact-list">
      <li class="contact-item contact-item--phone"><span class="contact-rule"></span>527.614.2870</li>
      <li class="contact-item contact-item--email"><span class="contact-rule"></span>rquillmore@lumaweb.net</li>
    </ul>
    <div class="owl-illustration" role="img" aria-label="Olive line drawing of a winking owl perched on a branch with flowers"></div>
  </section>
</body>
</html>
```